I am in need of both a Logo and Facebook Cover

The logo will be for a brand I am developing is for the brand "Sentiero Vanedo" The brand should exhibit a feeling of wealth, family and opportunity. It will be an educational group to teach people the keys to building wealthy lives. I want to place the logo inside the facebook cover. The facebook cover is for a facebook group. The group is "Sentiero Vanedo" the words wealth, family and opportunity should also be in the facebook cover.The design should be modern and motivating. Should give me the feeling of wealth and opportunity. Like a fancy high rise apartment building or exotic car. I want to feel hip, cool and rich
Updates

May want to create logo first as the logo should be on the Facebook cover Added Thursday, June 23, 2016

Target Market(s)

Entrepreneurs, business owners, primarily young adults, wealthy people, rich people

Logo Text

Sentiero Vanedo

Requirements
Must have
• Logo can be either written out or in Letters for example: SV The facebook cover should include the words wealth, family and opportunity. Should be a professional and powerful emotional feeling. Design should be modern and motivating. Should give me the feeling of wealth and opportunity. Like a fancy high rise apartment building or exotic car. I want to feel hip, cool and rich

```html
<!DOCTYPE html>
<html lang="en">
<head>
<meta charset="utf-8">
<title>Sentiero Vanedo — Cover and Logo</title>
<link rel="stylesheet" href="https://fonts.googleapis.com/css2?family=Jost:wght@300;400;500&display=swap">
<style>
  :root {
    --teal: #12b8cc;
    --white: #ffffff;
    --page: #ffffff;
    --sky-top: #6f8fae;
    --sky-mid: #4d6a86;
    --valley: #2e4256;
    --ground: #1b2733;
  }
  html, body {
    margin: 0;
    padding: 0;
    width: 1200px;
    height: 1200px;
    overflow: hidden;
    background: var(--page);
    font-family: "Jost", "Century Gothic", sans-serif;
  }
  .canvas {
    position: relative;
    width: 1200px;
    height: 1200px;
  }
  .cover {
    position: absolute;
    left: 171px;
    top: 167px;
    width: 844px;
    height: 281px;
    overflow: hidden;
  }
  .cover-scene {
    position: absolute;
    inset: 0;
    background: linear-gradient(180deg, var(--sky-top) 0%, var(--sky-mid) 38%, var(--valley) 70%, var(--ground) 100%);
  }
  .cover-scene::after {
    content: "";
    position: absolute;
    inset: 0;
    background: linear-gradient(90deg, rgba(20,28,38,0.45) 0%, rgba(20,28,38,0) 40%, rgba(20,28,38,0) 65%, rgba(20,28,38,0.35) 100%);
  }
  .cover-headline {
    position: absolute;
    left: 331px;
    top: 78px;
    width: 190px;
    margin: 0;
    color: var(--white);
    font-weight: 400;
    line-height: 1;
  }
  .headline-word {
    display: block;
    letter-spacing: -1px;
  }
  .headline-word--wealth { font-size: 54px; }
  .headline-word--family { font-size: 62px; margin-top: -8px; }
  .headline-rule {
    display: block;
    width: 180px;
    height: 4px;
    background: var(--teal);
    margin-top: 4px;
  }
  .headline-word--opportunity {
    font-size: 31px;
    color: var(--teal);
    font-weight: 300;
    margin-top: 8px;
    letter-spacing: -0.5px;
  }
  .brand {
    display: flex;
    align-items: center;
  }
  .brand-dot {
    display: block;
    border-radius: 50%;
    flex: none;
  }
  .brand-name {
    display: flex;
    flex-direction: column;
    font-weight: 400;
  }
  .brand-name .name-lead { text-transform: uppercase; letter-spacing: 0.5px; }
  .brand-name .name-tail { text-transform: lowercase; }

  .cover-brand {
    position: absolute;
    right: 31px;
    top: 27px;
    gap: 14px;
  }
  .cover-brand .brand-dot {
    width: 36px;
    height: 36px;
    background: var(--white);
  }
  .cover-brand .brand-name { color: var(--white); line-height: 0.85; }
  .cover-brand .name-lead { font-size: 29px; }
  .cover-brand .name-tail { font-size: 25px; }

  .logo {
    position: absolute;
    left: 358px;
    top: 892px;
    gap: 36px;
  }
  .logo .brand-dot {
    width: 92px;
    height: 92px;
    background: var(--teal);
  }
  .logo .brand-name { color: var(--teal); line-height: 0.85; }
  .logo .name-lead { font-size: 66px; }
  .logo .name-tail { font-size: 56px; }
</style>
</head>
<body>
<main class="canvas">
  <section class="cover">
    <div class="cover-scene" role="img" aria-label="Photograph of a misty mountain valley with rocky peaks under a pale blue sky"></div>
    <h1 class="cover-headline">
      <span class="headline-word headline-word--wealth">WEALTH</span>
      <span class="headline-word headline-word--family">FAMILY</span>
      <span class="headline-rule"></span>
      <span class="headline-word headline-word--opportunity">OPPORTUNITY</span>
    </h1>
    <div class="brand cover-brand">
      <span class="brand-dot"></span>
      <span class="brand-name"><span class="name-lead">Sentiero</span><span class="name-tail">Vanedo</span></span>
    </div>
  </section>

  <section class="brand logo">
    <span class="brand-dot"></span>
    <span class="brand-name"><span class="name-lead">Sentiero</span><span class="name-tail">Vanedo</span></span>
  </section>
</main>
</body>
</html>
```